Korrawa Tide Supply Business Cards

I need a business card design for my business. We specialise in supplying quality brand cleaning products for boats
Updates

Target Market(s)

local household people with personal boats

Industry/Entity Type

Business

Requirements
Must have
• Address - 14 Fenwick Crescent, Nickol WA 6714
Phone - 0417 382 905
Email - korrawatidesupply@mailhaven.com
Web - www.korrawatidesupply.com.au
Martin Quill
Director

Business logo is a must have
Nice to have
• Glossjet logo is optional but recommended as it shows what we do

```html
<!DOCTYPE html>
<html lang="en">
<head>
<meta charset="utf-8">
<title>Korrawa Tide Supply – Business Card</title>
<link href="https://fonts.googleapis.com/css2?family=Open+Sans:wght@400;600;700&display=swap" rel="stylesheet">
<style>
  :root {
    --navy: #0d4d8c;
    --orange: #f07a22;
    --white: #ffffff;
    --paper: #f3f4f5;
    --backdrop: #e4e6e9;
  }
  * { box-sizing: border-box; margin: 0; padding: 0; }
  html, body {
    width: 1200px;
    height: 1023px;
    overflow: hidden;
    background: var(--backdrop);
    font-family: "Open Sans", Arial, sans-serif;
  }
  .card {
    position: absolute;
    left: 220px;
    width: 760px;
    height: 434px;
    overflow: hidden;
    box-shadow: 0 8px 24px rgba(0,0,0,0.18);
  }
  .card--front { top: 60px; background: var(--paper); }
  .card--back  { top: 530px; background: var(--navy); }

  .card__band {
    position: absolute;
    inset: 0;
    width: 100%;
    height: 100%;
  }

  /* front */
  .brand {
    position: absolute;
    left: 68px;
    top: 92px;
    display: flex;
    align-items: center;
    gap: 16px;
  }
  .brand__dot {
    width: 35px;
    height: 35px;
    border-radius: 50%;
    background: var(--navy);
  }
  .brand__name {
    font-size: 34px;
    font-weight: 700;
    color: var(--navy);
    white-space: nowrap;
  }
  .person {
    position: absolute;
    left: 47px;
    top: 316px;
    color: var(--white);
  }
  .person__name {
    font-size: 23px;
    font-weight: 600;
    color: var(--orange);
    line-height: 1.15;
  }
  .person__title {
    font-size: 13px;
    line-height: 1.4;
  }
  .person__address {
    margin-top: 22px;
    font-size: 14px;
    white-space: nowrap;
  }
  .contact {
    position: absolute;
    left: 452px;
    top: 248px;
    list-style: none;
    color: var(--white);
    font-size: 14px;
  }
  .contact__item {
    display: flex;
    align-items: center;
    gap: 12px;
    height: 34px;
    white-space: nowrap;
  }
  .contact__icon {
    width: 16px;
    height: 16px;
    flex: none;
  }

  /* back */
  .back-brand {
    position: absolute;
    inset: 0;
    display: flex;
    align-items: center;
    justify-content: center;
    gap: 18px;
  }
  .back-brand__dot {
    width: 42px;
    height: 42px;
    border-radius: 50%;
    background: var(--white);
  }
  .back-brand__name {
    font-size: 40px;
    font-weight: 700;
    color: var(--white);
    white-space: nowrap;
  }
</style>
</head>
<body>
  <section class="card card--front" aria-label="Business card front">
    <svg class="card__band" viewBox="0 0 1000 572" preserveAspectRatio="none" aria-hidden="true">
      <path d="M0,360 C260,390 520,330 760,250 C860,218 940,200 1000,196 L1000,572 L0,572 Z" fill="var(--navy)"/>
    </svg>

    <div class="brand">
      <span class="brand__dot"></span>
      <span class="brand__name">Korrawa Tide Supply</span>
    </div>

    <div class="person">
      <p class="person__name">Martin Quill</p>
      <p class="person__title">Director</p>
      <p class="person__address">14 Fenwick Crescent, Nickol WA 6714</p>
    </div>

    <ul class="contact">
      <li class="contact__item">
        <svg class="contact__icon" viewBox="0 0 24 24" aria-hidden="true"><path fill="var(--orange)" d="M6.6 10.8a15.1 15.1 0 0 0 6.6 6.6l2.2-2.2a1 1 0 0 1 1-.25 11.4 11.4 0 0 0 3.6.57 1 1 0 0 1 1 1V20a1 1 0 0 1-1 1A17 17 0 0 1 3 4a1 1 0 0 1 1-1h3.5a1 1 0 0 1 1 1c0 1.25.2 2.45.57 3.57a1 1 0 0 1-.25 1z"/></svg>
        <span>0417 382 905</span>
      </li>
      <li class="contact__item">
        <svg class="contact__icon" viewBox="0 0 24 24" aria-hidden="true"><rect x="2.5" y="5" width="19" height="14" rx="1.5" fill="none" stroke="var(--orange)" stroke-width="2"/><path d="M3 6l9 7 9-7" fill="none" stroke="var(--orange)" stroke-width="2"/></svg>
        <span>korrawatidesupply@mailhaven.com</span>
      </li>
      <li class="contact__item">
        <svg class="contact__icon" viewBox="0 0 24 24" aria-hidden="true"><circle cx="12" cy="12" r="9.5" fill="none" stroke="var(--orange)" stroke-width="2"/><ellipse cx="12" cy="12" rx="4" ry="9.5" fill="none" stroke="var(--orange)" stroke-width="1.6"/><path d="M2.5 12h19M4 7h16M4 17h16" stroke="var(--orange)" stroke-width="1.4"/></svg>
        <span>www.korrawatidesupply.com.au</span>
      </li>
    </ul>
  </section>

  <section class="card card--back" aria-label="Business card back">
    <div class="back-brand">
      <span class="back-brand__dot"></span>
      <span class="back-brand__name">Korrawa Tide Supply</span>
    </div>
  </section>
</body>
</html>
```